Plate Rally! Digital Order Web App

This is a web app on mobile phone, for consumers to order food inside a restaurant using their phones. we have done up the flow but we need to revamp UI design. pls have a look at our current web on your mobile phone:
https://demo.tavrozi.app/o/KLMV/314725

CURRENT DESIGN.
1. food category on left side, always shown. menu items in list view with image.
2. when we click on an item, there is popup page, to select modifiers, or quantity.
3. order review page(cart page) is quite messy now, need a complete new look.
4 payment page(no need to design, handle by Quellon)
5. order confirmation page. success or error return

DESIGN requirements:
please browse through and click to order with current page above. we have put in lots of thoughts and effort for current flow, the new design should base on this flow.
1. web app. no zoom in/out is allowed for users. responsive html to suit different mobile phone screen size. modern fonts.
2. PAGES needed:
home/welcome page,
well laid out menu items page,
single item page, with add on choice and modifier
cart page(to include recommended items, ordered item list, remove item total, changeable quantity,
confirmation page(success, fail)

DELIVERABLES - responsive html, fonts, images asset such as icons, animation, button images(suitable for commercial use without further third party loyalty fee)
Updates

Hi all if we have left a comment on ur design, please revise accordingly and we will conclude it soon!

Target Market(s)

young diners who order food on their mobile phone.

Industry/Entity Type

Restaurant

Coding

Coded - Design and coding required

Number of Pages Required

5+ page

Colors

Designer to choose colors to be used in the design.

Requirements
Must have
• - lively, appetising colors while making the page easy to read. easy on eyes.
• - consistency. fonts used.
Nice to have
• - 2 color schemes
• - html codes. we will top up if you can deliver coded html.
Should not have
• - should not have more than 3 colors
• - should not have more than 3 different fonts
• - should not use colors that are dull

```html
<!DOCTYPE html>
<html lang="en">
<head>
<meta charset="utf-8">
<title>Plate Rally! – Single Item Screens</title>
<link rel="stylesheet" href="https://fonts.googleapis.com/css2?family=Raleway:wght@400;500;600;700&family=Noto+Sans+SC:wght@400&display=swap">
<style>
  :root {
    --stage: #e8e6e4;
    --panel: #ffffff;
    --panel-foot: #f9f9f9;
    --ink: #222222;
    --ink-soft: #333333;
    --muted: #8a8a8a;
    --rule: #d9d9d9;
    --accent: #f7434f;
    --accent-glow: rgba(247, 67, 79, 0.35);
    --radio-off: #bdbdbd;
    --photo-potato-a: #f6c445;
    --photo-potato-b: #d98a1c;
    --photo-octopus-a: #d8c29a;
    --photo-octopus-b: #a68a5c;
  }
  * { margin: 0; padding: 0; box-sizing: border-box; }
  html, body {
    width: 907px; height: 1200px; overflow: hidden;
    background: var(--stage);
    font-family: "Raleway", "Noto Sans SC", sans-serif;
    color: var(--ink);
  }
  .stage {
    position: relative; width: 766px; height: 1014px;
    transform: scale(1.18407); transform-origin: 0 0;
  }
  .screen { position: absolute; top: 0; background: var(--panel); overflow: hidden; }
  .screen--potato { left: 0; width: 355px; height: 850px; }
  .screen--octopus { left: 410px; width: 356px; height: 1014px; }
  .screen__foot { position: absolute; left: 0; right: 0; top: 790px; bottom: 0; background: var(--panel-foot); }
  .hero {
    position: absolute; left: 0; top: 0; width: 100%; height: 268px;
    border-radius: 0 0 22px 22px;
    box-shadow: 0 3px 4px rgba(0,0,0,0.35);
  }
  .hero--potato { background: radial-gradient(circle at 45% 45%, var(--photo-potato-a), var(--photo-potato-b)); }
  .hero--octopus { background: radial-gradient(circle at 60% 55%, var(--photo-octopus-a), var(--photo-octopus-b)); }
  .back-arrow { position: absolute; left: 8px; top: 10px; width: 36px; height: 26px; }
  .abs { position: absolute; white-space: nowrap; line-height: 1.2; }
  .item-title { font-size: 21px; font-weight: 700; letter-spacing: 0.2px; }
  .item-subtitle { font-family: "Noto Sans SC", sans-serif; font-size: 15px; color: var(--muted); }
  .rule { position: absolute; height: 1px; background: var(--rule); }
  .section-label { font-size: 16px; font-weight: 600; }
  .option-label { font-size: 14px; color: var(--ink-soft); }
  .hint { font-size: 12px; color: var(--ink-soft); }
  .hint em { font-style: normal; color: var(--accent); }
  .radio { position: absolute; width: 19px; height: 19px; border-radius: 50%; background: var(--radio-off); }
  .radio--on { background: var(--accent); box-shadow: 0 2px 6px var(--accent-glow); }
  .stepper__sign { position: absolute; color: var(--accent); font-size: 22px; line-height: 1; font-weight: 400; }
  .stepper__box {
    position: absolute; width: 42px; height: 25px; border: 1px solid var(--rule);
    background: var(--panel); font-size: 15px; text-align: center; line-height: 23px;
  }
  .total { font-size: 16px; font-weight: 700; }
  .total span { color: var(--accent); font-weight: 600; }
  .btn {
    position: absolute; height: 39px; border-radius: 3px;
    display: flex; align-items: center; justify-content: center;
    font-size: 14px; font-weight: 500;
  }
  .btn--outline { border: 1px solid var(--accent); background: var(--panel); color: var(--ink); }
  .btn--primary { background: var(--accent); color: #fff; font-weight: 600; }
  .modifier-title { font-size: 17px; font-weight: 500; color: var(--accent); }
  .modifier-hint { font-size: 10px; color: var(--muted); }
  .chevron { position: absolute; }
  .platter { font-size: 13px; color: var(--ink-soft); line-height: 21px; white-space: normal; width: 190px; }
  .price { font-size: 17px; font-weight: 500; }
</style>
</head>
<body>
<div class="stage">

  <section class="screen screen--potato">
    <div class="screen__foot"></div>
    <div class="hero hero--potato" role="img" aria-label="Photo of grilled potato chips on skewers with chilli seasoning"></div>
    <svg class="back-arrow" viewBox="0 0 36 26" fill="none" stroke="#fff" stroke-width="2.4"><path d="M34 13H3M14 2L3 13l11 11"/></svg>

    <h1 class="abs item-title" style="left:26px;top:297px">Grilled Potato Chip 3Pcs</h1>
    <p class="abs item-subtitle" style="left:26px;top:333px">烤土豆片</p>
    <div class="rule" style="left:26px;top:368px;width:266px"></div>

    <h2 class="abs section-label" style="left:26px;top:382px">Serve Order</h2>
    <p class="abs option-label" style="left:26px;top:421px">Serve first</p>
    <span class="radio" style="left:261px;top:421px"></span>
    <p class="abs option-label" style="left:26px;top:458px">Serve later</p>
    <span class="radio radio--on" style="left:261px;top:457px"></span>
    <p class="abs hint" style="left:26px;top:495px">Please make a selection for <em>serve order</em></p>
    <div class="rule" style="left:26px;top:528px;width:266px"></div>

    <h2 class="abs section-label" style="left:26px;top:547px">How many do you want ?</h2>
    <span class="stepper__sign" style="left:71px;top:582px">+</span>
    <span class="stepper__box" style="left:95px;top:580px">4</span>
    <span class="stepper__sign" style="left:144px;top:581px">−</span>

    <p class="abs total" style="left:27px;top:640px">Total : <span>$ 2.60</span></p>

    <a class="btn btn--outline" style="left:28px;top:707px;width:294px">Review</a>
    <a class="btn btn--primary" style="left:28px;top:759px;width:294px">Add to Cart</a>
  </section>

  <section class="screen screen--octopus">
    <div class="screen__foot"></div>
    <div class="hero hero--octopus" role="img" aria-label="Photo of grilled octopus balls on skewers over a bamboo mat"></div>
    <svg class="back-arrow" viewBox="0 0 36 26" fill="none" stroke="#fff" stroke-width="2.4"><path d="M34 13H3M14 2L3 13l11 11"/></svg>

    <h1 class="abs item-title" style="left:26px;top:300px">Grilled Octopus Ball</h1>
    <p class="abs item-subtitle" style="left:26px;top:334px">碳烤小章丸</p>

    <p class="abs modifier-title" style="left:26px;top:383px">Modifier one</p>
    <p class="abs modifier-hint" style="left:26px;top:405px">Choose one</p>
    <svg class="chevron" style="left:260px;top:396px" width="24" height="15" viewBox="0 0 24 15" fill="none" stroke="#999" stroke-width="1.3"><path d="M1 1l11 12L23 1"/></svg>
    <div class="rule" style="left:26px;top:422px;width:268px"></div>

    <p class="abs platter" style="left:42px;top:453px">Veg Platter A (egg ,<br>&nbsp;fishball bakchol )</p>
    <span class="radio" style="left:263px;top:468px"></span>
    <p class="abs platter" style="left:42px;top:510px">Veg Platter B (Chinese tofu ,<br>tungoh spinach )</p>
    <span class="radio radio--on" style="left:263px;top:520px"></span>
    <p class="abs platter" style="left:42px;top:568px">Veg Platter C (Shanghai<br>&nbsp;green, Spinach , Lettuce )</p>
    <span class="radio" style="left:263px;top:577px"></span>

    <p class="abs modifier-title" style="left:26px;top:637px">Modifier two</p>
    <p class="abs modifier-hint" style="left:26px;top:659px">Choose one</p>
    <svg class="chevron" style="left:268px;top:654px" width="10" height="15" viewBox="0 0 10 15" fill="none" stroke="#999" stroke-width="1.3"><path d="M1 1l7 6.5L1 14"/></svg>
    <div class="rule" style="left:26px;top:676px;width:268px"></div>

    <p class="abs modifier-title" style="left:26px;top:709px">Modifier three</p>
    <p class="abs modifier-hint" style="left:26px;top:731px">Choose one</p>
    <svg class="chevron" style="left:268px;top:726px" width="10" height="15" viewBox="0 0 10 15" fill="none" stroke="#999" stroke-width="1.3"><path d="M1 1l7 6.5L1 14"/></svg>
    <div class="rule" style="left:26px;top:748px;width:268px"></div>

    <p class="abs price" style="left:28px;top:788px">$ 14.80</p>
    <span class="stepper__sign" style="left:229px;top:787px">+</span>
    <span class="stepper__box" style="left:252px;top:785px">4</span>
    <span class="stepper__sign" style="left:300px;top:786px">−</span>

    <p class="abs hint" style="left:26px;top:837px">Please make a selection for <em>serve order</em></p>

    <a class="btn btn--outline" style="left:28px;top:886px;width:296px">Review</a>
    <a class="btn btn--primary" style="left:28px;top:938px;width:296px">Add to Cart</a>
  </section>

</div>
</body>
</html>
```